Spirit Animal illustration/message for Business Card Backs

We need 7 spirit animals illustrations and their corresponding message for the back of the business card based on the 7 charkas: Bear, Deer, Puma, Dolphin, Blue Heron, White Owl, Eagle. We would like the seven animals to be cohesive in design. Below is more information for each charka and the corresponding message:

Root Chakra:
Bear: Strength, Confidence, Grounding, Emotional Support, Connection to Earth
Message: “Feel your Rhythm become one with the Mother’s”

Sacral Chakra:
Deer: Compassion, Tenderness, Inner Strength, Agility, Grace, Renewal
Message: “Express your Passion for Life in every Adventure, large or small”

Solar Plexus Chakra:
Puma/Black Panther: Courage, Curiosity, Instinct, Honesty, Authenticity
Message: “Let your Integrity and Compassion guide your Actions”

Heart Chakra:
Dolphin: Playfulness, Wholeness, Heart Connection, Community
Message: “Feel yourself expand and embrace all Life”

Throat Chakra:
Blue Heron: Resourcefulness, Independence, Determination, Patience
Message: “Express your Truth and Love honoring your Inner Voice”

Third Eye Chakra:
White Owl: Intuition, Wisdom, Discernment, Hidden Potential, seeing through Illusions
Message: “Open yourself to the infinite possibilities of the Universe and create your Personal Wisdom”

Crown Chakra:
Eagle: Light, Spirit, Divine Guidance, Connection of Heart and Mind, Big Picture
Message: “Know and trust you are always divinely guided on your Path”
Updates

Need extra days to review

Target Market(s)

Radiant Body Fair

Industry/Entity Type

Wellness

Colors

Designer to choose colors to be used in the design.

Requirements
Must have
• The following Animals: Bear, Deer, Puma, Dolphin, Blue Heron, White Owl, Eagle
• Be geometric, orgamni. Should have a cutting edge feel.
Nice to have
• 2 dimensional would be cool
Should not have
• should not be childish

```html
<!DOCTYPE html>
<html lang="en">
<head>
<meta charset="utf-8">
<title>Spirit Animal Card Backs – Seven Chakras</title>
<link rel="stylesheet" href="https://fonts.googleapis.com/css2?family=Ultra&family=Raleway:ital,wght@0,700;1,300;1,400&display=swap">
<style>
  :root {
    --bg-light: #d4d4d4;
    --bg-dark: #8e8e8e;
    --card: #ffffff;
    --ink: #111111;
    --root: #d7262b;      --root-frame: #e89a98;
    --sacral: #f07b1d;    --sacral-frame: #f2d3a8;
    --solar: #f5b41b;     --solar-frame: #ece06a;
    --heart: #1f9148;     --heart-frame: #7dc9a0;
    --throat: #1b9fc4;    --throat-frame: #45b0d3;
    --third: #2a3d94;     --third-frame: #9aa3d0;
    --crown: #a1208f;     --crown-frame: #c9a6d4;
  }
  * { box-sizing: border-box; margin: 0; padding: 0; }
  html, body { width: 1200px; height: 1155px; overflow: hidden; }
  body {
    position: relative;
    background: radial-gradient(ellipse at 50% 55%, var(--bg-light) 0%, #b9b9b9 45%, var(--bg-dark) 100%);
    font-family: "Raleway", sans-serif;
  }
  .card {
    position: absolute;
    width: 316px; height: 316px;
    background: var(--card);
    border: 6px solid var(--frame);
    text-align: center;
  }
  .card--root   { --frame: var(--root-frame);   --accent: var(--root);   left: 78px;  top: 86px; }
  .card--sacral { --frame: var(--sacral-frame); --accent: var(--sacral); left: 441px; top: 86px; }
  .card--solar  { --frame: var(--solar-frame);  --accent: var(--solar);  left: 802px; top: 86px; }
  .card--heart  { --frame: var(--heart-frame);  --accent: var(--heart);  left: 78px;  top: 430px; }
  .card--throat { --frame: var(--throat-frame); --accent: var(--throat); left: 441px; top: 430px; }
  .card--third  { --frame: var(--third-frame);  --accent: var(--third);  left: 802px; top: 430px; }
  .card--crown  { --frame: var(--crown-frame);  --accent: var(--crown);  left: 441px; top: 772px; }

  .animal {
    position: absolute;
    left: 74px; top: 12px;
    width: 156px; height: 140px;
    border-radius: 4px;
    background: linear-gradient(150deg, #ffffff 0%, color-mix(in srgb, var(--accent) 30%, #fff) 55%, color-mix(in srgb, var(--accent) 55%, #fff) 100%);
  }
  .animal--wide { left: 48px; width: 208px; top: 30px; height: 90px; }

  .chakra-title {
    position: absolute; left: 0; right: 0; top: 158px;
    font-family: "Ultra", serif;
    font-weight: 400;
    font-size: 20px;
    letter-spacing: 0.5px;
    color: var(--accent);
  }
  .qualities {
    position: absolute; left: 20px; right: 20px; top: 196px;
    font-weight: 700; font-size: 12px; line-height: 15px; color: var(--ink);
  }
  .message {
    position: absolute; left: 14px; right: 14px; top: 238px;
    font-style: italic; font-weight: 300; font-size: 12px; line-height: 14.5px; color: var(--ink);
  }
  .quote {
    font-family: Georgia, serif; font-style: normal; font-weight: 700;
    color: var(--accent); font-size: 17px; line-height: 0;
  }
  .quote--open { vertical-align: 2px; margin-right: 3px; }
  .quote--close { vertical-align: -9px; margin-left: 3px; }
  .chakra-mark {
    position: absolute; left: 50%; top: 268px;
    width: 32px; height: 32px; margin-left: -16px;
    border-radius: 50%; background: var(--accent);
  }
</style>
</head>
<body>

<section class="card card--root">
  <div class="animal" role="img" aria-label="Geometric low-poly bear with pink and red triangles"></div>
  <h2 class="chakra-title">ROOT CHAKRA</h2>
  <p class="qualities">Strength, Confidence, Grounding, Emotional Support, Connection to Earth</p>
  <p class="message">Feel your Rhythm become<br>one with the Mother’s</p>
  <div class="chakra-mark"></div>
</section>

<section class="card card--sacral">
  <div class="animal" role="img" aria-label="Geometric low-poly deer with orange triangles"></div>
  <h2 class="chakra-title">SACRAL CHAKRA</h2>
  <p class="qualities">Compassion, Tenderness, Inner Strength, Agility, Grace, Renewal</p>
  <p class="message">Express your Passion for Life<br>in every Adventure, large or small</p>
  <div class="chakra-mark"></div>
</section>

<section class="card card--solar">
  <div class="animal animal--wide" role="img" aria-label="Geometric leaping puma with yellow and green triangles"></div>
  <h2 class="chakra-title">SOLAR PLEXUS CHAKRA</h2>
  <p class="qualities">Courage, Curiosity, Instinct, Honesty, Authenticity</p>
  <p class="message"><span class="quote quote--open">“</span>Let your Integrity and<br>Compassion guide your Actions<span class="quote quote--close">”</span></p>
  <div class="chakra-mark"></div>
</section>

<section class="card card--heart">
  <div class="animal animal--wide" role="img" aria-label="Geometric leaping dolphin with green triangles" style="height:120px;top:18px"></div>
  <h2 class="chakra-title">HEART CHAKRA</h2>
  <p class="qualities">Playfulness, Wholeness,<br>Heart Connection, Community</p>
  <p class="message"><span class="quote quote--open">“</span>Feel yourself expand and<br>embrace all Life<span class="quote quote--close">”</span></p>
  <div class="chakra-mark"></div>
</section>

<section class="card card--throat">
  <div class="animal" role="img" aria-label="Geometric standing blue heron with blue triangles"></div>
  <h2 class="chakra-title">THROAT CHAKRA</h2>
  <p class="qualities">Resourcefulness, Independence, Determination, Patience</p>
  <p class="message"><span class="quote quote--open">“</span>Express your Truth and<br>Love honoring your Inner Voice<span class="quote quote--close">”</span></p>
  <div class="chakra-mark"></div>
</section>

<section class="card card--third">
  <div class="animal" role="img" aria-label="Geometric white owl with indigo triangles"></div>
  <h2 class="chakra-title">THIRD EYE CHAKRA</h2>
  <p class="qualities">Intuition, Wisdom, Discernment, Hidden Potential, seeing through Illusions</p>
  <p class="message"><span class="quote quote--open">“</span>Open yourself to the infinite possibilities of the<br>Universe and create your Personal Wisdom<span class="quote quote--close">”</span></p>
  <div class="chakra-mark"></div>
</section>

<section class="card card--crown">
  <div class="animal" role="img" aria-label="Geometric eagle head with violet triangles"></div>
  <h2 class="chakra-title">CROWN CHAKRA</h2>
  <p class="qualities">Light, Spirit, Divine Guidance, Connection of Heart and Mind, Big Picture</p>
  <p class="message"><span class="quote quote--open">“</span>Know and trust you are always<br>divinely guided on your Path<span class="quote quote--close">”</span></p>
  <div class="chakra-mark"></div>
</section>

</body>
</html>
```